Gym Menu

Hi,

I would like to create a menu for my fitness center/ Dance school.

I do have a picture of how i would like it to look like ill attach it down there and instead of the Mexican looking icons i would like to have gym related icons example (Bar bell, dumbbells, etc..)

The menu will consist of the following

Smoothies
- Lagoon Waltz (20 SR)
(Kiwi, Pineapple, Banana, Grapes)
-Coral Drift (20 SR)
(Orange, Peach, Pineapple)
-Tidy Kick (20 SR)
(Carrot, Mango, Orange)
-Purple Thunder (20 SR)
(Blackberry, Raspberry, Banana)
-Cool Breeze (20 SR)
( Lemonade, Mint)
-Ruby Lantern (20 SR)
(Lemonade, Strawberry, Mint)

Mean Green Juices

-Quick Sprout (20SR)
(Cucumber, Celery, Green Apple, Spinach, Lemon, Ginger)
-Hop To It Now! (20 SR)
(Carrots, Apple, Beetroot)

Shake It Up

-Dusky Swirl (20 SR)
(Mocha, Skimmed Milk)

- Velvet Tumbler
(Chocolate, Skimmed Milk)

-Big Lift Zest

(Peanut Butter, Honey, Skimmed Milk, Banana) (20 SR)

Yummy Bites

- Zataar Croissant (10 SR)
- Cheese Croissant (10 SR)
- Plane Croissant (10 SR)
- Blueberry Muffin (7 SR)
- Chocolate Muffin (7 SR)
- Vanilla Muffin (7SR)
- Cookies (7 SR)
- Brownie (10 SR)
-Fresh Berry Popsicle (10 SR)
- Fresh Orange Popsicle (10 SR)

Make it Lite

-Garden Salad (15 SR)
-Greek Salad (15 SR)
-Ceaser Salad (15 SR)
-Italian Salad (15 SR)
- Tuna Sandwich (25 SR)
- Turkey Sandwich (25 SR)
- Chicken Sandwich (25 SR)
-Happy Patch Bowls (8SR)
- Mixed Nuts (10 SR)

Coffee and tea
- Americano (10 SR)
- Espresso (10 SR)
- Turkish Coffee (10 SR)
- Cappuccino (15 SR)
- Cafe Latte (15 SR)
-Hot Cacao (15 SR)
-Extra shor + 5SR

- Green Tea (10 SR)
- Earl Grey (10 SR)
- English Breakfast (10SR)

• The gyms color is orange ... i want this to be in the menu

the gyms name is vartomel i also want this in big somewhere

Colors of the menu should be

Orange
Yellow
green
red

all shades

```html
<!DOCTYPE html>
<html lang="en">
<head>
<meta charset="utf-8">
<title>Gym Menu</title>
<link rel="stylesheet" href="https://fonts.googleapis.com/css2?family=Alfa+Slab+One&family=Roboto+Slab:wght@800&display=swap">
<style>
:root{
  --kraft:#dcc3a3;
  --kraft-edge:#d2b692;
  --orange:#f7932a;
  --yellow:#ffd23a;
  --green:#5ff23a;
  --green-frame:#7ef05a;
  --green-pale:#c5f2a8;
  --red:#c4122a;
  --ink:#222;
  --divider:#6f6a66;
}
*{margin:0;padding:0;box-sizing:border-box}
html,body{width:1200px;height:851px;overflow:hidden}
body{background:var(--kraft)}
.menu{position:relative;width:1200px;height:851px;background:radial-gradient(ellipse at 50% 50%,var(--kraft) 60%,var(--kraft-edge) 100%);overflow:hidden}
.frames{position:absolute;inset:0}
.title{position:absolute;font-family:"Alfa Slab One",serif;font-weight:400;line-height:.92;text-transform:uppercase;white-space:nowrap}
.items{position:absolute;list-style:none;font-family:"Roboto Slab",serif;font-weight:800;font-size:12.5px;line-height:19.6px;text-transform:uppercase;letter-spacing:.2px}
.smoothies-title{left:50px;top:46px;font-size:80px;line-height:92px;color:var(--green)}
.smoothies-list{left:290px;top:50px;color:var(--green);width:252px}
.shake-title{left:42px;top:372px;font-size:58px;color:var(--red);letter-spacing:1px}
.shake-up{left:322px;top:392px;font-size:150px;color:var(--red);letter-spacing:-8px}
.shake-list{left:42px;top:448px;color:var(--red);line-height:19px}
.shake-list li{margin-bottom:16px}
.juices-title{left:40px;top:645px;font-size:50px;color:var(--orange)}
.juices-title span{display:block;margin-top:12px}
.juices-list{left:264px;top:700px;color:var(--green);width:278px;line-height:18.5px}
.bites-title{left:654px;top:38px;font-size:58px;color:var(--red);line-height:1.05}
.bites-list{left:870px;top:96px;color:var(--red)}
.brand-name{position:absolute;left:640px;top:292px;font-family:"Alfa Slab One",serif;font-size:26px;color:var(--orange);letter-spacing:1px}
.lite-title{left:640px;top:362px;font-size:66px;color:var(--orange);line-height:1.05}
.lite-list{left:904px;top:366px;color:var(--red);width:236px}
.coffee-title{position:absolute;left:750px;top:626px;font-family:"Alfa Slab One",serif;font-size:28px;color:var(--red)}
.coffee-a{left:652px;top:676px;color:var(--red);line-height:18.5px}
.coffee-b{left:892px;top:666px;color:var(--red);line-height:18.5px}
.icon{position:absolute}
.icon-barbell{left:630px;top:210px;width:125px;height:62px}
.icon-whistle{left:904px;top:750px;width:92px;height:40px}
</style>
</head>
<body>
<main class="menu">
  <svg class="frames" width="1200" height="851" viewBox="0 0 1200 851" aria-hidden="true">
    <line x1="601" y1="0" x2="601" y2="851" stroke="var(--divider)" stroke-width="2"/>
    <polygon points="30,12 546,10 549,326 556,350 30,340" fill="none" stroke="var(--orange)" stroke-width="7"/>
    <polygon points="30,638 550,632 548,826 32,828" fill="none" stroke="var(--green-pale)" stroke-width="6"/>
    <polygon points="636,22 1180,20 1178,306 836,312 832,152 640,150" fill="none" stroke="var(--yellow)" stroke-width="7"/>
    <polygon points="618,352 1148,348 1146,578 622,576" fill="none" stroke="var(--green-frame)" stroke-width="7"/>
  </svg>

  <h1 class="title smoothies-title">Smo<br>oth<br>ies</h1>
  <ul class="items smoothies-list">
    <li>– Lagoon Waltz (20 SR) (Kiwi, Pineapple, Banana, Grapes)</li>
    <li>–Coral Drift (20 SR) (Orange, Peach, Pineapple)</li>
    <li>–Tidy Kick (20 SR) (Carrot, Mango, Orange)</li>
    <li>–Purple Thunder (20 SR) (Blackberry, Raspberry, Banana)</li>
    <li>–Cool Breeze (20 SR) (Lemonade, Mint)</li>
    <li>–Ruby Lantern (20 SR) (Lemonade, Strawberry, Mint)</li>
  </ul>

  <h2 class="title shake-title">Shake It</h2>
  <div class="title shake-up">Up</div>
  <ul class="items shake-list">
    <li>–Dusky Swirl (20 SR)<br>(Mocha, Skimmed Milk)</li>
    <li>– Velvet Tumbler<br>(Chocolate, Skimmed Milk)</li>
    <li>–Big Lift Zest<br>(Peanut Butter, Honey, Skimmed Milk, Banana) (20 SR)</li>
  </ul>

  <h2 class="title juices-title">Mean Green<span>Juices</span></h2>
  <ul class="items juices-list">
    <li>–Quick Sprout (20SR)<br>(Cucumber, Celery, Green Apple, Spinach, Lemon, Ginger)</li>
    <li>–Hop To It Now! (20 SR)<br>(Carrots, Apple, Beetroot)</li>
  </ul>

  <h2 class="title bites-title">Yummy<br>Bites</h2>
  <ul class="items bites-list">
    <li>– Zataar Croissant (10 SR)</li>
    <li>– Cheese Croissant (10 SR)</li>
    <li>– Plane Croissant (10 SR)</li>
    <li>– Blueberry Muffin (7 SR)</li>
    <li>– Chocolate Muffin (7 SR)</li>
    <li>– Vanilla Muffin (7SR)</li>
    <li>– Cookies (7 SR)</li>
    <li>– Brownie (10 SR)</li>
    <li>–Fresh Berry Popsicle (10 SR)</li>
    <li>– Fresh Orange Popsicle (10 SR)</li>
  </ul>
  <div class="icon icon-barbell" role="img" aria-label="Barbell icon">
    <svg width="125" height="62" viewBox="0 0 125 62"><rect x="0" y="24" width="125" height="14" rx="7" fill="var(--ink)"/></svg>
  </div>
  <p class="brand-name">VARTOMEL</p>

  <h2 class="title lite-title">Make<br>It<br>Lite</h2>
  <ul class="items lite-list">
    <li>–Garden Salad (15 SR)</li>
    <li>–Greek Salad (15 SR)</li>
    <li>–Ceaser Salad (15 SR)</li>
    <li>–Italian Salad (15 SR)</li>
    <li>– Tuna Sandwich (25 SR)</li>
    <li>– Turkey Sandwich (25 SR)</li>
    <li>– Chicken Sandwich (25 SR)</li>
    <li>–Happy Patch Bowls (8SR)</li>
    <li>– Mixed Nuts (10 SR)</li>
  </ul>

  <h2 class="coffee-title">COFFEE &amp; TEA</h2>
  <ul class="items coffee-a">
    <li>– Americano (10 SR)</li>
    <li>– Espresso (10 SR)</li>
    <li>– Turkish Coffee (10 SR)</li>
    <li>– Cappuccino (15 SR)</li>
    <li>– Cafe Latte (15 SR)</li>
    <li>–Hot Cacao (15 SR)</li>
    <li>–Extra Shor + 5SR</li>
  </ul>
  <ul class="items coffee-b">
    <li>– Green Tea (10 SR)</li>
    <li>– Earl Grey (10 SR)</li>
    <li>– English Breakfast (10SR)</li>
  </ul>
  <div class="icon icon-whistle" role="img" aria-label="Coach whistle icon">
    <svg width="92" height="40" viewBox="0 0 92 40"><rect x="0" y="4" width="92" height="34" rx="17" fill="var(--red)"/></svg>
  </div>
</main>
</body>
</html>
```